ZRD Roofing Billboard Design

Looking for a fresh new billboard design with my new headshot photo and using some info from my previous billboard and maybe website for design/content inspiration. My website is https://zrdroofing.com/

Also attached are my logo and current lawn sign design. I am looking for something simple, clean and modern. The landing page website should be 3816tops.com like my previous billboard has.

```html
<!DOCTYPE html>
<html lang="en">
<head>
<meta charset="utf-8">
<title>ZRD Roofing Billboard</title>
<link rel="stylesheet" href="https://fonts.googleapis.com/css2?family=Roboto+Slab:wght@400;500;700;800&family=Roboto:wght@500;700&display=swap">
<style>
  :root {
    --page-bg: #efefef;
    --board-bg: #ffffff;
    --navy: #13283f;
    --green: #4caf4a;
    --white: #ffffff;
    --photo-top: #c89c84;
    --photo-mid: #b9c7e0;
    --photo-bottom: #a9b8d6;
  }
  * { margin: 0; padding: 0; box-sizing: border-box; }
  html, body {
    width: 1200px;
    height: 1200px;
    overflow: hidden;
    background: var(--page-bg);
  }
  .billboard {
    position: absolute;
    left: 40px;
    top: 367px;
    width: 1120px;
    height: 466px;
    background: var(--board-bg);
    overflow: hidden;
  }
  .billboard__bands {
    position: absolute;
    left: 0;
    top: 0;
    width: 1120px;
    height: 466px;
  }
  .headline {
    position: absolute;
    left: 60px;
    color: var(--navy);
    font-family: "Roboto Slab", serif;
    line-height: 1;
    white-space: nowrap;
  }
  .headline--top { top: 64px; font-size: 54px; font-weight: 500; }
  .headline--top .headline__strong { font-size: 76px; font-weight: 800; }
  .headline--mid { top: 134px; font-size: 58px; font-weight: 500; letter-spacing: -0.5px; }
  .headline--price { top: 198px; font-size: 54px; font-weight: 500; }
  .headline__price {
    color: var(--green);
    font-size: 66px;
    font-weight: 700;
    margin-left: 12px;
  }
  .contact {
    position: absolute;
    left: 60px;
    color: var(--white);
    font-family: "Roboto", sans-serif;
    font-weight: 700;
    white-space: nowrap;
    line-height: 1;
  }
  .contact--phone { top: 322px; font-size: 62px; }
  .contact--web { top: 398px; font-size: 27px; font-weight: 500; letter-spacing: 3.4px; }
  .brand {
    position: absolute;
    left: 564px;
    top: 64px;
    width: 200px;
    text-align: center;
    color: var(--navy);
    font-family: "Roboto Slab", serif;
  }
  .brand__name {
    display: block;
    font-size: 18px;
    font-weight: 500;
    line-height: 1.2;
  }
  .brand__mark {
    display: block;
    width: 46px;
    height: 46px;
    margin: 8px auto 10px;
    border-radius: 50%;
    background: var(--green);
  }
  .brand__tagline {
    display: block;
    font-size: 12px;
    font-weight: 500;
    white-space: nowrap;
  }
  .headshot {
    position: absolute;
    left: 726px;
    top: 50px;
    width: 444px;
    height: 416px;
  }
</style>
</head>
<body>
  <div class="billboard">
    <svg class="billboard__bands" viewBox="0 0 1120 466" aria-hidden="true">
      <rect x="0" y="298" width="1120" height="168" fill="var(--navy)"/>
      <polygon points="0,298 614,298 557,466 0,466" fill="var(--green)"/>
    </svg>

    <div class="headline headline--top">FULL <span class="headline__strong">ROOF</span></div>
    <div class="headline headline--mid">REPLACEMENTS</div>
    <div class="headline headline--price">Starting at<span class="headline__price">$7,499</span></div>

    <div class="contact contact--phone">(555) 214-7390</div>
    <div class="contact contact--web">www.zrdroofing.com</div>

    <div class="brand">
      <span class="brand__name">ZRD Roofing LLC</span>
      <span class="brand__mark"></span>
      <span class="brand__tagline">Premium Roof Replacement Specialists</span>
    </div>

    <svg class="headshot" viewBox="0 0 444 416" role="img" aria-label="Headshot of the company owner, smiling, in a light blue button-down shirt">
      <defs>
        <linearGradient id="headshotFill" x1="0" y1="0" x2="0" y2="1">
          <stop offset="0" stop-color="var(--photo-top)"/>
          <stop offset="0.35" stop-color="var(--photo-mid)"/>
          <stop offset="1" stop-color="var(--photo-bottom)"/>
        </linearGradient>
      </defs>
      <path d="M0,416 L0,190 Q0,150 40,140 L140,108 L140,0 L300,0 L300,108 L400,140 Q444,150 444,190 L444,416 Z" fill="url(#headshotFill)"/>
    </svg>
  </div>
</body>
</html>
```